REDESIGN MAIN BANNER IMAGE FOR MARKETING WEBSITE

I feel like my main banner image is too busy but I like it but i want to see other options. www.brightlanepromoworks.biz I want a nice professional clean design that goes with current theme of site. Must look professional and show the variety of incentives we offer but not be overwelming.

My business is called Brightlane Promo Works and I provide businesses around the world with marketing incentives that they can use to create exciting promotions and contest and marketing giveaways to help attract more customers.

I provide a variety of different types of incentives such as Vacation Certificates, Dining Vouchers, Hotel Savings Cards, Smart Watches, Etc. that businesses can use in their marketing efforts.

I want my main banner image to reflect the variety of different categories of incentives... that I offer here: https://www.brightlanepromoworks.biz/incentives

We can use images of certificates or images.....I just want the content to be the same:

CONTENT FOR MAIN BANNER IMAGE:
INCREASE LEADS AND SALES OVERNIGHT

CREATE EXCITING MARKETING PROMOTIONS GIVING AWAY SMART DEVICES, VACATION CERTIFICATES, DINING VOUCHERS AND OTHER INCENTIVES TO YOUR CUSTOMERS

GET A FREE SAMPLE PACKAGE FOR A LIMITED TIME ONLY

Target Market(s)

b2b business owners, ceo, president, owner, founder

Industry/Entity Type

Promotional

Requirements
Must have
• Hi guys keep in mind the finished product will have to be 1800x840

Nice to have
• I want a nice professional clean design that goes with current theme of site. Must look professional and show the variety of incentives we offer but not be overwelming.
Should not have

```html
<!DOCTYPE html>
<html lang="en">
<head>
<meta charset="utf-8">
<title>Brightlane Promo Works – Increase Leads &amp; Sales Overnight</title>
<link href="https://fonts.googleapis.com/css2?family=Archivo+Black&family=Days+One&family=Oswald:wght@500;700&family=Roboto+Condensed:wght@400;700&display=swap" rel="stylesheet">
<style>
:root{
  --red:#d0121b;
  --red-dark:#b30d15;
  --blue:#0e5aa7;
  --white:#ffffff;
  --ink:#1b1b1b;
  --grey:#8c8c8c;
  --line:#d4d4d4;
  --green:#3fc42f;
  --green-dark:#2a9f1f;
  --floor:#ececec;
}
*{box-sizing:border-box;margin:0;padding:0}
html,body{width:1200px;height:560px;overflow:hidden}
body{background:linear-gradient(#ffffff 0%,#ffffff 55%,var(--floor) 100%);font-family:"Days One",sans-serif;position:relative}
.banner-bg{position:absolute;left:0;top:0}

.headline{position:absolute;left:24px;width:1152px;top:0;height:109px;display:flex;align-items:center;justify-content:center;
  font-family:"Archivo Black",sans-serif;font-size:47px;color:var(--white);letter-spacing:-.3px;white-space:nowrap}
.promo-copy{position:absolute;left:150px;width:900px;top:122px;text-align:center;color:var(--white);font-size:17px;line-height:1.4;letter-spacing:-.2px}

.incentives{position:absolute;left:0;width:1200px;top:186px;display:flex;justify-content:center;gap:54px}
.incentive{display:flex;align-items:center;gap:12px;color:var(--white)}
.incentive svg{width:40px;height:40px;flex:none}
.incentive-label{font-size:15px;line-height:1.1}

/* certificate cards */
.flyer{position:absolute;top:292px;width:150px;height:168px;background:var(--white);box-shadow:0 3px 10px rgba(0,0,0,.25);
  display:flex;flex-direction:column;overflow:hidden;font-family:"Roboto Condensed",sans-serif}
.fl-head{height:46px;padding:7px 9px 0;flex:none}
.fl-kicker{font-family:"Oswald",sans-serif;font-weight:500;font-size:9px;color:var(--grey);letter-spacing:.5px;white-space:nowrap}
.fl-title{margin-top:3px;font-family:"Oswald",sans-serif;font-weight:700;font-size:16px;line-height:1;color:var(--ink);white-space:nowrap}
.fl-title b{background:var(--red);color:var(--white);padding:0 4px;margin-left:3px;font-weight:700}
.fl-photo{height:64px;flex:none}
.fl-band{height:16px;flex:none;background:var(--red);color:var(--white);font-size:8px;font-weight:700;padding:0 9px;display:flex;align-items:center;white-space:nowrap}
.fl-body{flex:1;padding:8px 9px 0}
.fl-line{height:4px;background:var(--line);margin-bottom:6px}
.fl-foot{height:16px;flex:none;border-top:1px solid var(--line);color:var(--red);font-size:7.5px;font-weight:700;display:flex;align-items:center;justify-content:center;white-space:nowrap}

.flyer.featured{left:505px;top:268px;width:190px;height:192px;z-index:5;box-shadow:0 4px 14px rgba(0,0,0,.3)}
.featured .fl-head{height:52px}
.featured .fl-kicker{font-size:10px}
.featured .fl-title{font-size:20px}
.featured .fl-photo{height:74px}

.cta{position:absolute;left:455px;top:472px;width:290px;height:48px;border-radius:6px;
  background:linear-gradient(var(--green),var(--green-dark));color:var(--white);font-size:18px;
  display:flex;align-items:center;justify-content:center;box-shadow:0 3px 8px rgba(0,0,0,.3);z-index:20;text-decoration:none;white-space:nowrap}
.cta-note{position:absolute;left:0;width:1200px;top:530px;text-align:center;font-size:12px;color:var(--red);letter-spacing:.6px}
</style>
</head>
<body>

<svg class="banner-bg" width="1200" height="300" viewBox="0 0 1200 300" aria-hidden="true">
  <path d="M24 109 H1176 V222 C1176 236 1168 242 1150 240 Q600 298 50 240 C32 242 24 236 24 222 Z" fill="var(--blue)"/>
  <rect x="24" y="0" width="1152" height="109" fill="var(--red)"/>
</svg>

<h1 class="headline">INCREASE LEADS &amp; SALES OVERNIGHT</h1>
<p class="promo-copy">Create exciting marketing promotions giving away smart devices, vacation certificates, dining vouchers and other incentives to your customers</p>

<div class="incentives">
  <div class="incentive">
    <svg viewBox="0 0 50 50" fill="#fff" aria-hidden="true">
      <rect x="10" y="2" width="30" height="22" rx="2"/><rect x="13" y="5" width="24" height="16" fill="var(--blue)"/>
      <rect x="16" y="16" width="14" height="28" rx="2"/><rect x="18" y="19" width="10" height="20" fill="var(--blue)"/>
      <rect x="32" y="30" width="16" height="4"/><rect x="32" y="37" width="16" height="10" rx="1"/>
      <rect x="4" y="28" width="10" height="14" rx="2"/>
    </svg>
    <span class="incentive-label">Smart<br>Devices</span>
  </div>
  <div class="incentive">
    <svg viewBox="0 0 50 50" aria-hidden="true">
      <path d="M2 10 H48 V20 A5 5 0 0 0 48 30 V40 H2 V30 A5 5 0 0 0 2 20 Z" fill="#fff"/>
      <text x="25" y="35" text-anchor="middle" font-family="Archivo Black,sans-serif" font-size="24" fill="var(--blue)">%</text>
    </svg>
    <span class="incentive-label">Dining<br>Vouchers</span>
  </div>
  <div class="incentive">
    <svg viewBox="0 0 50 50" aria-hidden="true">
      <rect x="1" y="4" width="46" height="34" fill="#fff"/>
      <rect x="4" y="7" width="40" height="28" fill="none" stroke="var(--blue)" stroke-width="1.2"/>
      <rect x="8" y="12" width="32" height="2.5" fill="var(--blue)"/><rect x="8" y="18" width="26" height="2.5" fill="var(--blue)"/><rect x="8" y="24" width="18" height="2.5" fill="var(--blue)"/>
      <circle cx="37" cy="34" r="7" fill="#fff" stroke="var(--blue)" stroke-width="2"/>
      <path d="M33 40 L33 49 L37 46 L41 49 L41 40" fill="#fff"/>
    </svg>
    <span class="incentive-label">Vacation<br>Certificates</span>
  </div>
  <div class="incentive">
    <svg viewBox="0 0 50 50" fill="#fff" aria-hidden="true">
      <rect x="3" y="14" width="44" height="10"/><rect x="6" y="26" width="38" height="22"/>
      <rect x="22" y="14" width="6" height="34" fill="var(--blue)"/>
      <path d="M25 14 C18 2 8 6 14 13 M25 14 C32 2 42 6 36 13" fill="none" stroke="#fff" stroke-width="3"/>
    </svg>
    <span class="incentive-label">Other<br>Incentives</span>
  </div>
</div>

<article class="flyer" style="left:173px">
  <div class="fl-head"><p class="fl-kicker">DINING VOUCHER</p><p class="fl-title">ENJOY<b>$25 OFF</b></p></div>
  <div class="fl-photo" role="img" aria-label="Photo of diners sharing a meal" style="background:linear-gradient(#3a2418,#8a5a36 55%,#d9b48a)"></div>
  <div class="fl-band">EXCLUSIVELY FOR: CUSTOMER NAME</div>
  <div class="fl-body"><div class="fl-line"></div><div class="fl-line" style="width:70%"></div></div>
  <div class="fl-foot">WWW.PERKHARBORREWARDS.COM</div>
</article>

<article class="flyer" style="left:339px">
  <div class="fl-head"><p class="fl-kicker">YOUR BRAND NEW</p><p class="fl-title"><b style="margin-left:0">HD TABLET</b></p></div>
  <div class="fl-photo" role="img" aria-label="Photo of a tablet device" style="background:linear-gradient(#1a1a1a,#3c3c3c 60%,#8a8a8a)"></div>
  <div class="fl-band">EXCLUSIVELY FOR: CUSTOMER NAME</div>
  <div class="fl-body"><div class="fl-line"></div><div class="fl-line" style="width:70%"></div></div>
  <div class="fl-foot">WWW.PERKHARBORREWARDS.COM</div>
</article>

<article class="flyer featured">
  <div class="fl-head"><p class="fl-kicker">AN ALL INCLUSIVE</p><p class="fl-title">ENJOY<b>RESORT STAY</b></p></div>
  <div class="fl-photo" role="img" aria-label="Photo of a tropical island resort" style="background:linear-gradient(#78c0e8,#2e8fc0 45%,#e0d2a2)"></div>
  <div class="fl-band">EXCLUSIVELY FOR: CUSTOMER NAME</div>
  <div class="fl-body"><div class="fl-line"></div><div class="fl-line" style="width:70%"></div></div>
  <div class="fl-foot">WWW.PERKHARBORREWARDS.COM</div>
</article>

<article class="flyer" style="left:711px">
  <div class="fl-head"><p class="fl-kicker">AIRFARE WITH</p><p class="fl-title">ENJOY<b>HOTEL</b></p></div>
  <div class="fl-photo" role="img" aria-label="Photo of a passenger jet in a blue sky" style="background:linear-gradient(#2d6fb3,#8fc2e8 60%,#e6eef5)"></div>
  <div class="fl-band">EXCLUSIVELY FOR: CUSTOMER NAME</div>
  <div class="fl-body"><div class="fl-line"></div><div class="fl-line" style="width:70%"></div></div>
  <div class="fl-foot">WWW.PERKHARBORREWARDS.COM</div>
</article>

<article class="flyer" style="left:877px">
  <div class="fl-head"><p class="fl-kicker">YOUR BRAND NEW</p><p class="fl-title"><b style="margin-left:0">SMARTWATCH</b></p></div>
  <div class="fl-photo" role="img" aria-label="Photo of a person exercising with a fitness watch" style="background:linear-gradient(#d6d6d6,#8e8e8e)"></div>
  <div class="fl-band">EXCLUSIVELY FOR: CUSTOMER NAME</div>
  <div class="fl-body"><div class="fl-line"></div><div class="fl-line" style="width:70%"></div></div>
  <div class="fl-foot">WWW.PERKHARBORREWARDS.COM</div>
</article>

<a class="cta" href="https://www.brightlanepromoworks.biz/incentives">Get A Free Sample Package</a>
<p class="cta-note">FOR A LIMITED TIME ONLY</p>

</body>
</html>
```